Brightcurve Laser Lipo Brochure

Need a 3 panel brochure
Full Colour
Sales/info brochure
Photos provided
Testimonials
Product Specs - http://brightcurvetone.example/brightcurvetone/request-a-demo/opportunity.aspx
Brightcurve Laser Lipo is trademarked
Website and contact details
description of what about the technique-
http://brightcurvetone.example/brightcurvetone/laser-lipo.aspx
Examples of successful clinics - to follow

Also require business card to compliment the brochure

Target Market(s)

Target Audience Clinics, Gyms, Salons

Industry/Entity Type

Business

Requirements
Must have
• website www.brightcurvetone.example
testimonials
"After just two laser-lipo sessions I was happily surprised to find that I had dropped between one and two belt sizes ..... dinewatch.example.au MTK"
"I have been a number of the laser lipo treatments and using the VTN cream in between session with great results. Have lost 4cm around waist. Highly recommend.....dinewatch.example.au SandraP"

```html
<!DOCTYPE html>
<html lang="en">
<head>
<meta charset="utf-8">
<title>Brightcurve Laser Lipo Brochure</title>
<link rel="stylesheet" href="https://fonts.googleapis.com/css2?family=Mukta:wght@400;600;700&family=Playfair+Display:wght@400;500&display=swap">
<style>
  :root {
    --magenta: #b0325f;
    --sky: #29abe2;
    --navy: #141b2c;
    --ink: #4a4a4a;
    --paper: #ffffff;
    --rule: #9aa3b3;
  }
  * { box-sizing: border-box; margin: 0; padding: 0; }
  html, body { width: 1200px; height: 849px; overflow: hidden; background: var(--paper); }
  body { font-family: "Mukta", sans-serif; }
  .brochure { position: relative; width: 1200px; height: 849px; overflow: hidden; }

  /* Panel 1 – testimonials */
  .panel-testimonials { position: absolute; left: 0; top: 0; width: 400px; height: 849px; background: var(--paper); }
  .section-title { position: absolute; top: 163px; width: 400px; text-align: center; color: var(--sky); font-size: 24px; font-weight: 600; }
  .pill { display: inline-block; background: var(--magenta); color: var(--paper); border-radius: 10px; font-weight: 600; text-align: center; }
  .panel-testimonials .pill { position: absolute; left: 142px; top: 199px; width: 122px; height: 38px; line-height: 40px; font-size: 17px; }
  .quote { position: absolute; left: 70px; width: 300px; color: var(--ink); font-size: 14px; line-height: 20px; text-align: center; }
  .quote-one { top: 265px; }
  .quote-two { top: 410px; }
  .quote .mark { font-family: "Playfair Display", serif; font-size: 34px; line-height: 0; color: #666; vertical-align: -12px; }
  .photo-skin-small { position: absolute; left: 0; top: 698px; width: 400px; height: 151px; background: linear-gradient(100deg, #3a2224 0%, #6e4640 55%, #3b2528 100%); }

  /* Panel 2 – map & contact */
  .panel-contact { position: absolute; left: 400px; top: 0; width: 401px; height: 849px; background: var(--navy); }
  .panel-contact .band { position: absolute; left: 0; top: 0; width: 401px; height: 620px; background: var(--magenta); }
  .map { position: absolute; left: 32px; top: 138px; width: 323px; height: 289px; border-radius: 14px; background: linear-gradient(135deg, #ffffff 0%, #e8f4fb 100%); }
  .contact-card { position: absolute; left: 49px; top: 427px; width: 292px; height: 350px; background: var(--sky); border-radius: 0 0 16px 16px; color: var(--paper); padding: 46px 22px 0; font-size: 15px; line-height: 20px; }
  .pin-dot { position: absolute; left: 137px; top: 4px; width: 18px; height: 18px; border-radius: 50%; background: var(--magenta); }
  .clinic-name { font-weight: 700; font-size: 14px; letter-spacing: .2px; margin-bottom: 22px; }
  .hours { font-weight: 500; font-size: 16px; line-height: 21px; margin-bottom: 16px; }
  .person { font-weight: 700; font-size: 15px; }
  .contact-list { list-style: none; font-size: 13.5px; line-height: 19px; }
  .contact-list .label { color: var(--magenta); }

  /* Panel 3 – cover */
  .panel-cover { position: absolute; left: 801px; top: 0; width: 399px; height: 849px; }
  .photo-cover { position: absolute; inset: 0; background: radial-gradient(ellipse at 75% 45%, #8a6a66 0%, #4a3438 40%, #1b1f30 80%); }
  .brand-title { position: absolute; left: 32px; top: 555px; color: var(--paper); font-family: "Playfair Display", serif; font-weight: 500; font-size: 66px; line-height: 66px; letter-spacing: 2px; }
  .tagline { position: absolute; left: 34px; top: 695px; width: 345px; color: var(--paper); font-size: 14.5px; line-height: 17px; font-weight: 500; }
  .panel-cover .pill { position: absolute; left: 34px; top: 788px; width: 121px; height: 36px; line-height: 38px; font-size: 17px; }

  .rules { position: absolute; left: 0; top: 0; width: 1200px; height: 849px; pointer-events: none; }
</style>
</head>
<body>
<main class="brochure">

  <section class="panel-testimonials">
    <h2 class="section-title">Testimonials</h2>
    <span class="pill">Laser Lipo</span>
    <p class="quote quote-one"><span class="mark">&ldquo;</span>After just two laser-lipo sessions I was happily surprised to find that I had dropped between one and two belt sizes ..... dinewatch.example.au MTK <span class="mark">&rdquo;</span></p>
    <p class="quote quote-two"><span class="mark">&ldquo;</span>I have been a number of the laser lipo treatments and using the VTN cream in between session with great results. Have lost 4cm around waist. Highly recommend.....dinewatch.example.au SandraP <span class="mark">&rdquo;</span></p>
    <div class="photo-skin-small" role="img" aria-label="Close-up photo of skin with a red lipstick kiss mark"></div>
  </section>

  <section class="panel-contact">
    <div class="band"></div>
    <div class="map" role="img" aria-label="Street map showing the clinic location"></div>
    <div class="contact-card">
      <span class="pin-dot"></span>
      <h3 class="clinic-name">MARLAS BRIGHTCURVE LIPO CLINIC</h3>
      <p class="hours">Hours of Operation<br>Mon - Fri 8am - 7pm<br>Saturday 8am - 2pm</p>
      <p class="person">MARLA</p>
      <ul class="contact-list">
        <li><span class="label">T |</span> 0412 555 907</li>
        <li><span class="label">ADRESS |</span> 14c Harbour View Rd - Rear Entrance, Westmere 6090</li>
        <li><span class="label">WEBSITE |</span> www.brightcurvetone.example</li>
        <li><span class="label">E-MAIL |</span> marla@brightcurvetone.example</li>
      </ul>
    </div>
  </section>

  <section class="panel-cover">
    <div class="photo-cover" role="img" aria-label="Photo of a woman's side torso in a white top with a red lipstick kiss mark on the skin"></div>
    <h1 class="brand-title">BRIGHT<br>CURVE</h1>
    <p class="tagline">A revolutionary new procedure for instant and permanent cm-loss, cellulite reduction and skin tightening using state of the art laser technology. PAIN FREE, NON INVASIVE, LOSE CM'S IN MINUTES!</p>
    <span class="pill">Laser Lipo</span>
  </section>

  <svg class="rules" viewBox="0 0 1200 849" aria-hidden="true">
    <g stroke="var(--rule)" stroke-width="1">
      <line x1="0" y1="650" x2="470" y2="650"/>
      <line x1="0" y1="659" x2="470" y2="659"/>
      <line x1="0" y1="670" x2="470" y2="670"/>
      <line x1="750" y1="645" x2="828" y2="645"/>
      <line x1="750" y1="656" x2="828" y2="656"/>
      <line x1="750" y1="668" x2="828" y2="668"/>
    </g>
  </svg>

</main>
</body>
</html>
```